Business Card Design

We would like to re-design our business cards. Our Company - Qoralin Turbochargers, rebuilds turbochargers and sells replacement parts. Our website is: http://www.qoralinturbochargers-example.com
We just had our logo changed. I will attach the file. Looking for fresh new/modern business card. We like the colors red, black, white and silver. Black background looks attractive, but not a requirement. The final design should communicate reasonable/competitive prices, top quality and reliability of our products.
Updates
Project Deadline Extended
Reason: Need to finalize the info on the card. Currently working on changing address and email info. Want to make sure it is the correct one before accepting the final design. Unless, this is something that can be changed at a later time..??
Industry/Entity Type
Business
Contact Information for Business Card
QORALIN TURBOCHARGERS, LLC
20473 Pemberly Road NE
Massillon, OH 44012
Tel: +1-330-555-0162
Fax: +1-330-555-0187
info@QoralinTurbochargers-example.com
Our current business card had the following highlights:
*We rebuild all Turbocharges for Automotive, Diesel and Industrial
*Precision Balancing and in-house turbocharger needs
*All Turbocharger replacement parts are made in USA / U.K.
Look and feel
Each slider illustrates characteristics of the customer's brand and the style your logo design should communicate.

```html
<!DOCTYPE html>
<html lang="en">
<head>
<meta charset="utf-8">
<title>Qoralin Turbochargers – Business Card</title>
<link href="https://fonts.googleapis.com/css2?family=Open+Sans:wght@400;600;700;800&display=swap" rel="stylesheet">
<style>
  :root {
    --stage: #2b2623;
    --card: #121212;
    --card-edge: #1d1d1d;
    --red: #e3232a;
    --white: #ffffff;
    --muted: #d9d9d9;
    --rule: #3a3a3a;
  }
  * { box-sizing: border-box; margin: 0; padding: 0; }
  html, body {
    width: 1200px; height: 844px; overflow: hidden;
    background: var(--stage);
    font-family: "Open Sans", Arial, sans-serif;
  }
  .stage {
    position: relative; width: 1200px; height: 844px;
    display: flex; align-items: center; justify-content: center; gap: 60px;
  }
  .card {
    position: relative; width: 525px; height: 300px;
    background: var(--card);
    border: 1px solid var(--card-edge);
    box-shadow: 0 12px 30px rgba(0,0,0,.45);
  }
  /* front side */
  .brand {
    position: absolute; left: 150px; top: 62px;
    display: flex; align-items: center; gap: 12px;
    white-space: nowrap;
  }
  .brand-dot { width: 22px; height: 22px; border-radius: 50%; background: var(--red); flex: none; }
  .brand-name {
    color: var(--white); font-weight: 800; font-size: 26px; letter-spacing: .2px;
  }
  .person {
    position: absolute; left: 24px; top: 168px; width: 232px; text-align: right;
    white-space: nowrap;
  }
  .person-name { color: var(--white); font-weight: 600; font-size: 22px; line-height: 1.1; }
  .person-role { color: var(--red); font-size: 15px; margin-top: 2px; }
  .person-address { color: var(--muted); font-size: 15px; line-height: 1.3; margin-top: 12px; }
  .divider {
    position: absolute; left: 272px; top: 150px; width: 1px; height: 110px;
    background: var(--rule);
  }
  .contact { position: absolute; left: 290px; top: 152px; list-style: none; }
  .contact li {
    display: flex; align-items: center; gap: 10px;
    color: var(--muted); font-size: 14px; height: 24px;
    white-space: nowrap;
  }
  .icon {
    width: 16px; height: 16px; background: var(--red); border-radius: 2px;
    display: flex; align-items: center; justify-content: center; flex: none;
  }
  /* back side */
  .card-back { display: flex; align-items: center; justify-content: center; }
  .back-brand { display: flex; align-items: center; gap: 14px; white-space: nowrap; }
  .back-brand .brand-dot { width: 30px; height: 30px; }
  .back-brand .brand-name { font-size: 34px; }
</style>
</head>
<body>
<main class="stage">
  <section class="card card-front" aria-label="Business card front">
    <div class="brand">
      <span class="brand-dot"></span>
      <span class="brand-name">Qoralin Turbochargers</span>
    </div>

    <div class="person">
      <p class="person-name">Jonah Whitfield</p>
      <p class="person-role">Managing Director</p>
      <p class="person-address">27814, Foundry Lane West<br>Brenmoor City, 552190</p>
    </div>

    <div class="divider"></div>

    <ul class="contact">
      <li>
        <span class="icon"><svg width="10" height="10" viewBox="0 0 10 10"><path d="M2 1 L4 1 L4.6 3 L3.4 3.8 Q4.2 5.6 6.2 6.6 L7 5.4 L9 6 L9 8 Q5 9 2.5 6 Q0.8 3.5 2 1Z" fill="#fff"/></svg></span>
        (044)-555-0148
      </li>
      <li>
        <span class="icon"><svg width="10" height="10" viewBox="0 0 10 10"><rect x="2.5" y="1" width="5" height="3" fill="#fff"/><rect x="1" y="4" width="8" height="4" rx="1" fill="#fff"/><rect x="3" y="6" width="4" height="3" fill="#e3232a" stroke="#fff" stroke-width=".8"/></svg></span>
        123-555-0176
      </li>
      <li>
        <span class="icon"><svg width="10" height="10" viewBox="0 0 10 10"><rect x="1" y="2.5" width="8" height="5" fill="none" stroke="#fff" stroke-width="1"/><path d="M1 2.5 L5 6 L9 2.5" fill="none" stroke="#fff" stroke-width="1"/></svg></span>
        info@qoralin-example.com
      </li>
      <li>
        <span class="icon"><svg width="10" height="10" viewBox="0 0 10 10"><path d="M4 6 L6 4 M3.5 4.5 L2 6 A1.4 1.4 0 0 0 4 8 L5.5 6.5 M6.5 5.5 L8 4 A1.4 1.4 0 0 0 6 2 L4.5 3.5" fill="none" stroke="#fff" stroke-width="1.1"/></svg></span>
        www.qoralin-example.com
      </li>
    </ul>
  </section>

  <section class="card card-back" aria-label="Business card back">
    <div class="back-brand">
      <span class="brand-dot"></span>
      <span class="brand-name">Qoralin Turbochargers</span>
    </div>
  </section>
</main>
</body>
</html>
```